BRIGHTWAVE PARTNERS NAMECARD

Need to design a name card with an existing logo.

As we are professional corporate services provider our name card has to project a professional image.
Should be corporate, simple & professional.

Our corporate color is maroon red but not too dull.

Please refer to our website at www.brightwavepartners.com.sg

Would attach our logo herewith.

Front surface of namecard details:
BRIGHTWAVE PARTNERS PTE LTD
Registration No. 208731945K

Lowe Hui Ting CA (Singapore)
Director

Tel +65 6481 2957
Mobile +65 9172 3806
lowe@brightwavepartners.com.sg
www.brightwavepartners.com.sg

47 Palmer Lane
#07-14 Harbourlight Plaza
Singapore 274153

Back of namecard:-
OUR CORE SERVICES
Incorporation services
Corporate Secretarial Services
Accountancy service
Goods & Services Taxation
Corporate & Personal Taxation
Financial Reporting
Payroll Administration

AFFILIATES:
TRIVANTA CORPORATE SERVICES PTE LTD
BRIGHTWAVEREGISTRYPTE LTD
ORR MANAGEMENT SERVICES PTE LTD
DW LIM AND COMPANY PTE LTD
LEDGERWISE ACADEMY

```html
<!DOCTYPE html>
<html lang="en">
<head>
<meta charset="utf-8">
<title>Brightwave Partners Name Card</title>
<link rel="stylesheet" href="https://fonts.googleapis.com/css2?family=Tinos:wght@400;700&display=swap">
<style>
  :root {
    --backdrop: #e9e9e7;
    --card-white: #ffffff;
    --panel-grey: #b5c5c1;
    --brand-red: #d6163b;
    --edge-black: #111111;
    --ink: #111111;
  }
  html, body {
    margin: 0;
    padding: 0;
    width: 1200px;
    height: 857px;
    overflow: hidden;
    background: var(--backdrop);
  }
  .name-card {
    position: absolute;
    left: 50px;
    top: 72px;
    width: 1100px;
    height: 712px;
    display: block;
    box-shadow: 0 2px 10px rgba(0,0,0,0.12);
  }
  .card-base { fill: var(--card-white); }
  .info-panel { fill: var(--panel-grey); }
  .accent-crescent { fill: var(--brand-red); }
  .accent-edge { fill: none; stroke: var(--edge-black); stroke-width: 2.4; }
  .holder-name {
    font-family: "Tinos", "Times New Roman", serif;
    font-weight: 700;
    font-size: 40px;
    fill: var(--brand-red);
  }
  .holder-title {
    font-family: "Tinos", "Times New Roman", serif;
    font-weight: 700;
    font-size: 17px;
    fill: var(--brand-red);
  }
  .contact-line {
    font-family: "Tinos", "Times New Roman", serif;
    font-size: 16.5px;
    fill: var(--ink);
  }
  .contact-icon { fill: var(--ink); }
  .contact-icon-stroke { fill: none; stroke: var(--ink); stroke-width: 1.3; }
  .company-name {
    font-family: "Tinos", "Times New Roman", serif;
    font-weight: 400;
    font-size: 28px;
    fill: var(--brand-red);
  }
</style>
</head>
<body>
<svg class="name-card" viewBox="0 0 850 550" xmlns="http://www.w3.org/2000/svg">
  <rect class="card-base" x="0" y="0" width="850" height="550"/>
  <path class="info-panel" d="M0 0 L430 0 C505 115 510 375 355 550 L0 550 Z"/>
  <path class="accent-crescent" d="M430 0 L455 0 C538 125 540 382 360 550 L355 550 C510 375 505 115 430 0 Z"/>
  <path class="accent-edge" d="M456 0 C540 125 542 383 362 550"/>

  <text class="holder-name" x="213" y="134" text-anchor="middle">Lowe Hui Ting CA</text>
  <text class="holder-title" x="213" y="158" text-anchor="middle">Director</text>

  <g class="contact-group contact-group--phone">
    <path class="contact-icon" d="M30 302 q1.5 -2 3 -0.5 l2 2.5 q1 1.5 -0.5 2.5 l-1 0.8 q1.5 3.5 5 5 l0.8 -1 q1 -1.5 2.5 -0.5 l2.5 2 q1.5 1.5 -0.5 3 q-2 1.5 -4 0.5 q-7 -3 -10 -10 q-1 -2 0.5 -4 Z"/>
    <text class="contact-line" x="57" y="305">Tel +65 6481 2957</text>
    <text class="contact-line" x="57" y="326">Mobile +65 9172 3806</text>
  </g>

  <g class="contact-group contact-group--web">
    <circle class="contact-icon-stroke" cx="37" cy="364" r="7"/>
    <ellipse class="contact-icon-stroke" cx="37" cy="364" rx="3" ry="7"/>
    <line class="contact-icon-stroke" x1="30" y1="364" x2="44" y2="364"/>
    <line class="contact-icon-stroke" x1="31.5" y1="360" x2="42.5" y2="360"/>
    <line class="contact-icon-stroke" x1="31.5" y1="368" x2="42.5" y2="368"/>
    <text class="contact-line" x="57" y="359">lowe@brightwavepartners.com.sg</text>
    <text class="contact-line" x="57" y="380">www.brightwavepartners.com.sg</text>
  </g>

  <g class="contact-group contact-group--address">
    <path class="contact-icon" d="M37 424 c-4 0 -6.5 3 -6.5 6.5 c0 4.5 6.5 11 6.5 11 s6.5 -6.5 6.5 -11 c0 -3.5 -2.5 -6.5 -6.5 -6.5 Z M37 428 a2.6 2.6 0 1 1 0 5.2 a2.6 2.6 0 1 1 0 -5.2 Z" fill-rule="evenodd"/>
    <text class="contact-line" x="57" y="413">47 Palmer Lane</text>
    <text class="contact-line" x="57" y="433">#07-14 Harbourlight Plaza</text>
    <text class="contact-line" x="57" y="453">Singapore 274153</text>
    <text class="contact-line" x="57" y="479">Registration No. 208731945K</text>
  </g>

  <text class="company-name" x="692" y="281" text-anchor="middle">Brightwave Partners</text>
</svg>
</body>
</html>
```